UK landscaping company needs website

We, Brackwell Landscapes need a website design for a company based in Surrey, UK. The design should be bold and playful. We have three main areas of work driveways, paving and fencing. It shouldn't be too heavy in text and concentrate on the pictures from previous jobs we've completed. You may use stock images for the design, these can be changed if you are successful. Please don’t just copy the flyer it is just there to provide content.
We have a logo design which we would also like editing slightly.
Here are some of my local competitors
https://www.fernivalelandscapes.co.uk/

https://www.twinbirchgardendesign.com/

https://mallowbecklandscapes.co.uk/

Industry/Entity Type

Landscaping

Coding

Coded - Design and coding required

Number of Pages Required

3 page

Font styles to use
Sans Serif

Requirements
Must have
• Pictures of my previous jobs.
Must be mobile friendly
Easy to navigate
Nice to have
• Try to use different colours. It would be good to have some designs that aren’t just black and green.
I’d like some curves in the design.
Should not have
• We install hard landscaping. Think more building/construction and less plants and cutting grass.

```html
<!DOCTYPE html>
<html lang="en">
<head>
<meta charset="utf-8">
<title>Brackwell Landscapes</title>
<link href="https://fonts.googleapis.com/css2?family=Nunito:wght@600;700;800;900&family=Lato:wght@400;700&display=swap" rel="stylesheet">
<style>
:root{
  --sky:#94e3ff;
  --black:#000;
  --dark:#262626;
  --green:#6cbe45;
  --green-deep:#5aa832;
  --white:#fff;
  --text:#333;
  --muted:#777;
  --navy:#1f2a6b;
  --card:#f1f4f8;
  --line:#d9d9d9;
}
*{margin:0;padding:0;box-sizing:border-box}
html,body{width:1200px;height:4000px;overflow:hidden}
body{background:var(--sky);font-family:'Lato',sans-serif;color:var(--text);position:relative}
.abs{position:absolute}
.page{position:absolute;left:76px;top:92px;width:1048px;height:3814px;background:var(--white);overflow:hidden}
/* everything below is placed in canvas coordinates */
.site{position:absolute;left:-76px;top:-92px;width:1200px;height:4000px}

/* header */
.header{position:absolute;left:76px;top:92px;width:1048px;height:97px;background:var(--black)}
.brand{position:absolute;left:205px;top:122px;color:var(--white);font-family:'Nunito',sans-serif;font-weight:900;font-size:22px;line-height:1;letter-spacing:.3px;display:flex;align-items:center;gap:8px}
.brand-dot{width:12px;height:12px;border-radius:50%;background:var(--green)}
.nav{position:absolute;top:156px;left:541px;display:flex;gap:0;font-family:'Nunito',sans-serif;font-weight:700;font-size:10px;color:var(--white)}
.nav a{color:inherit;text-decoration:none;position:absolute;white-space:nowrap}
.nav .active{color:var(--green)}
.btn-contact{position:absolute;left:883px;top:140px;width:127px;height:31px;border-radius:16px;background:var(--green);color:var(--white);font-family:'Nunito',sans-serif;font-weight:800;font-size:10px;display:flex;align-items:center;justify-content:center}

/* hero */
.hero{position:absolute;left:76px;top:189px;width:1048px;height:587px;background:linear-gradient(180deg,#8fb94a 0%,#6a9a2e 35%,#4f7d22 60%,#8a8680 85%,#7b6e68 100%)}
.hero-title{position:absolute;left:76px;top:428px;width:1048px;text-align:center;color:var(--white);font-family:'Nunito',sans-serif;font-weight:900;font-size:44px;line-height:52px;text-shadow:0 2px 6px rgba(0,0,0,.35)}

/* about */
.about-photo{position:absolute;left:182px;top:886px;width:330px;height:415px;border:4px solid var(--green);background:var(--white);padding:3px}
.about-photo .ph{width:100%;height:calc(50% - 1px)}
.ph-top{background:linear-gradient(160deg,#4d5b3a,#6f7a4c 50%,#5b4a3a)}
.ph-bot{margin-top:2px;background:linear-gradient(160deg,#3d6a2a,#63a23a 60%,#b8a088)}
.eyebrow{position:absolute;left:552px;top:897px;color:var(--green);font-family:'Nunito',sans-serif;font-weight:800;font-size:10px}
.eyebrow::after{content:"";position:absolute;left:0;top:15px;width:58px;height:2px;background:var(--green)}
.about-title{position:absolute;left:557px;top:920px;font-family:'Nunito',sans-serif;font-weight:800;font-size:31px;color:var(--black)}
.about-copy{position:absolute;left:562px;top:980px;width:438px;font-size:11.2px;line-height:16.3px;color:var(--text)}
.about-copy p{margin-bottom:16px}
.stats{position:absolute;left:569px;top:1218px;display:flex;gap:0}
.stat{position:absolute;display:flex;align-items:center;gap:10px;white-space:nowrap}
.stat-ico{width:32px;height:32px;border-radius:50%;background:var(--green);display:flex;align-items:center;justify-content:center}
.stat-num{font-family:'Nunito',sans-serif;font-weight:800;font-size:11px;color:var(--black);position:relative}
.stat-num::after{content:"";position:absolute;left:0;top:16px;width:12px;height:2px;background:var(--green)}
.stat-lbl{font-size:5.5px;color:var(--muted);margin-top:9px}

/* services */
.section-title{position:absolute;left:76px;width:1048px;text-align:center;font-family:'Nunito',sans-serif;font-weight:900;font-size:31px;color:var(--green)}
.card{position:absolute;top:1498px;width:266px;height:228px;background:var(--green);color:var(--white);text-align:center}
.card-ico{position:absolute;left:88px;top:-47px;width:90px;height:90px;border-radius:50%;background:var(--white);border:3px solid var(--green);display:flex;align-items:center;justify-content:center}
.card h3{margin-top:50px;font-family:'Nunito',sans-serif;font-weight:900;font-size:27px;line-height:32px}
.card p{margin:8px auto 0;width:232px;font-size:11px;line-height:16.4px}
.card-btn{position:absolute;left:71px;bottom:-15px;width:124px;height:31px;border-radius:16px;background:var(--white);border:2px solid var(--green);color:var(--green);font-family:'Nunito',sans-serif;font-weight:800;font-size:11px;display:flex;align-items:center;justify-content:center}

/* projects */
.projects{position:absolute;left:76px;top:1827px;width:1048px;height:780px;background:var(--dark)}
.projects-title{position:absolute;left:124px;top:1858px;font-family:'Nunito',sans-serif;font-weight:900;font-size:33px;color:var(--green);letter-spacing:.5px}
.filters{position:absolute;top:1880px;left:467px;display:flex;gap:6px}
.pill{height:20px;padding:0 12px;border:2px solid var(--green);border-radius:10px;color:var(--white);font-family:'Nunito',sans-serif;font-weight:800;font-size:7.5px;display:flex;align-items:center;justify-content:center;min-width:58px}
.pill.on{background:var(--green)}
.proj-arrows{position:absolute;left:990px;top:1878px;display:flex;gap:14px}
.projects-rule{position:absolute;left:135px;top:1916px;width:939px;height:3px;background:var(--green)}
.tile{position:absolute;width:304px;height:302px}

/* faq */
.h2{position:absolute;font-family:'Nunito',sans-serif;font-weight:700;font-size:23px;color:#111}
.h2::after{content:"";position:absolute;left:0;top:40px;width:34px;height:3px;background:var(--green)}
.acc{position:absolute;left:214px;width:366px;height:32px;border-radius:16px;background:var(--green);color:var(--white);font-family:'Nunito',sans-serif;font-weight:700;font-size:9.5px;display:flex;align-items:center;justify-content:space-between;padding:0 16px 0 20px}
.acc.open{background:var(--dark)}
.acc span.sign{font-size:18px;font-weight:600;line-height:1}
.acc-body{position:absolute;left:234px;top:2883px;width:330px;font-size:9.4px;line-height:16px;color:var(--muted)}
.field{position:absolute;border:1px solid var(--line);border-radius:3px;background:var(--white);font-size:8.5px;color:var(--muted);padding:0 12px;display:flex;align-items:center}
.submit{position:absolute;left:878px;top:3031px;width:108px;height:31px;border-radius:16px;background:var(--green);color:var(--white);font-family:'Nunito',sans-serif;font-weight:700;font-size:9.5px;display:flex;align-items:center;justify-content:center}

/* testimonials */
.t-eyebrow{position:absolute;left:76px;width:1048px;top:3165px;text-align:center;font-size:7px;color:#7b6bd4}
.t-title{position:absolute;left:76px;width:1048px;top:3186px;text-align:center;font-family:'Nunito',sans-serif;font-weight:600;font-size:24px;line-height:33px;color:var(--navy)}
.t-card{position:absolute;left:397px;top:3332px;width:460px;height:179px;background:var(--card)}
.t-photo{position:absolute;left:343px;top:3293px;width:143px;height:199px;background:linear-gradient(170deg,#e9d8c4,#c9a98a 45%,#5c5048)}
.t-quote{position:absolute;left:742px;top:3308px}
.t-text{position:absolute;left:514px;top:3374px;width:300px;font-size:11.5px;line-height:19px;color:#8a8f98}
.t-stars{position:absolute;left:514px;top:3447px;font-size:7px;color:#f0a020;letter-spacing:1px}
.t-name{position:absolute;left:514px;top:3460px;font-size:8.5px;color:var(--navy)}

/* footer */
.footer{position:absolute;left:76px;top:3562px;width:1048px;height:344px;background:var(--black);color:var(--white)}
.f-brand{position:absolute;left:155px;top:3608px;font-family:'Nunito',sans-serif;font-weight:900;font-size:34px;color:var(--white);line-height:1;display:flex;align-items:center;gap:10px}
.f-brand .brand-dot{width:18px;height:18px}
.f-contact{position:absolute;left:155px;top:3705px;font-family:'Nunito',sans-serif;font-weight:700;font-size:15px;line-height:19.5px;color:var(--white)}
.f-contact div{display:flex;align-items:center;gap:8px}
.f-nav{position:absolute;left:480px;top:3592px;font-family:'Nunito',sans-serif;font-weight:700;font-size:18.5px;line-height:26.5px;color:var(--white)}
.f-notify{position:absolute;left:650px;width:430px;top:3596px;text-align:center}
.f-notify h4{font-family:'Nunito',sans-serif;font-weight:700;font-size:26px;line-height:32px}
.f-notify p{font-size:8.5px;margin-top:2px}
.f-input{position:absolute;left:663px;top:3666px;width:406px;height:33px;border-radius:17px;background:var(--white);font-size:7.5px;color:#aaa;padding-left:16px;display:flex;align-items:center}
.f-btn{position:absolute;left:950px;top:3666px;width:119px;height:33px;border-radius:17px;background:var(--green);color:var(--white);font-family:'Nunito',sans-serif;font-weight:800;font-size:8px;display:flex;align-items:center;justify-content:center}
.f-copy{position:absolute;left:650px;width:430px;top:3713px;text-align:center;font-size:6px;color:#bbb}
</style>
</head>
<body>
<div class="site">

  <!-- header -->
  <header class="header"></header>
  <div class="brand"><span class="brand-dot"></span>Brackwell Landscapes</div>
  <nav class="nav">
    <a class="active" style="left:0">Home</a>
    <a style="left:49px">Our Services</a>
    <a style="left:129px">About Us</a>
    <a style="left:204px">Our Projects</a>
    <a style="left:280px">FAQ</a>
  </nav>
  <div class="btn-contact">Contact Us Today</div>

  <!-- hero -->
  <section class="hero" role="img" aria-label="Sunlit garden with a curving block-paved path through a lawn, trees and flowering shrubs"></section>
  <h1 class="hero-title">Award Winning Driveways, Paving<br>and Fencing Contractor</h1>

  <!-- about -->
  <div class="abs" style="left:76px;top:776px;width:1048px;height:1051px;background:var(--white)"></div>
  <div class="about-photo">
    <div class="ph ph-top" role="img" aria-label="Overgrown garden before work begins"></div>
    <div class="ph ph-bot" role="img" aria-label="Same garden after, with fresh lawn and paved border"></div>
  </div>
  <div class="eyebrow">About US</div>
  <h2 class="about-title">Welcome To Brackwell Landscapes</h2>
  <div class="about-copy">
    <p>Lorem ipsum dolor sit amet, consectetur adipiscing elit, sed do eiusmod tempor incididunt ut labore et dolore magna aliqua. Quis ipsum suspendisse ultrices gravida. Risus commodo viverra maecenas accumsan lacus vel facilisis.</p>
    <p>Lorem ipsum dolor sit amet, consectetur adipiscing elit, sed do eiusmod tempor incididunt ut labore et dolore magna aliqua. Quis ipsum suspendisse ultrices gravida. Risus commodo viverra maecenas accumsan lacus vel facilisis.</p>
    <p>Lorem ipsum dolor sit amet, consectetur adipiscing elit, sed do eiusmod tempor incididunt ut labore et dolore magna aliqua. Quis ipsum suspendisse ultrices gravida. Risus commodo viverra maecenas accumsan lacus vel facilisis.</p>
  </div>
  <div class="stats">
    <div class="stat" style="left:0">
      <div class="stat-ico"><svg width="14" height="14" viewBox="0 0 14 14" fill="none" stroke="#fff" stroke-width="1.4"><circle cx="7" cy="7" r="5.5"/><path d="M4.5 8.5c1.4 1.4 3.6 1.4 5 0"/></svg></div>
      <div><div class="stat-num">1900</div><div class="stat-lbl">Happy Clients</div></div>
    </div>
    <div class="stat" style="left:100px">
      <div class="stat-ico"><svg width="14" height="14" viewBox="0 0 14 14" fill="none" stroke="#fff" stroke-width="1.4"><path d="M4 2h6v10l-3-2-3 2z"/></svg></div>
      <div><div class="stat-num">1900</div><div class="stat-lbl">Receive Awards</div></div>
    </div>
    <div class="stat" style="left:200px">
      <div class="stat-ico"><svg width="14" height="14" viewBox="0 0 14 14" fill="none" stroke="#fff" stroke-width="1.4"><rect x="2" y="2" width="4" height="4"/><rect x="8" y="2" width="4" height="4"/><rect x="2" y="8" width="4" height="4"/><rect x="8" y="8" width="4" height="4"/></svg></div>
      <div><div class="stat-num">2500</div><div class="stat-lbl">Finished Work</div></div>
    </div>
  </div>

  <!-- services -->
  <h2 class="section-title" style="top:1386px">Our Services</h2>
  <div class="card" style="left:199px">
    <div class="card-ico"><svg width="50" height="40" viewBox="0 0 50 40"><path d="M6 36 C18 34 30 30 32 24 C34 18 18 18 20 12 C22 6 34 5 44 6 L44 11 C36 11 28 12 28 14 C28 18 44 18 42 26 C40 34 24 38 6 38Z" fill="#000"/></svg></div>
    <h3>Driveways</h3>
    <p>Lorem ipsum dolor sit amet, consectetur adipiscing elit, sed do eiusmod tempor incididunt ut labore et dolore magna aliqua. Quis ipsum suspendisse ultrices gravida. Risus commodo viverra maecenas accumsan lacus vel facilisis.</p>
    <div class="card-btn">Read More</div>
  </div>
  <div class="card" style="left:467px">
    <div class="card-ico"><svg width="54" height="36" viewBox="0 0 54 36" fill="#000"><rect x="2" y="10" width="50" height="3"/><rect x="2" y="26" width="50" height="3"/><g><rect x="3" y="4" width="3" height="30"/><rect x="9" y="4" width="3" height="30"/><rect x="15" y="4" width="3" height="30"/><rect x="21" y="4" width="3" height="30"/><rect x="27" y="4" width="3" height="30"/><rect x="33" y="4" width="3" height="30"/><rect x="39" y="4" width="3" height="30"/><rect x="45" y="4" width="3" height="30"/></g></svg></div>
    <h3>Fencing</h3>
    <p>Lorem ipsum dolor sit amet, consectetur adipiscing elit, sed do eiusmod tempor incididunt ut labore et dolore magna aliqua. Quis ipsum suspendisse ultrices gravida. Risus commodo viverra maecenas accumsan lacus vel facilisis.</p>
    <div class="card-btn">Read More</div>
  </div>
  <div class="card" style="left:737px">
    <div class="card-ico"><svg width="42" height="42" viewBox="0 0 42 42" fill="none" stroke="#000" stroke-width="3"><rect x="3" y="3" width="36" height="36"/><path d="M3 21L21 3L39 21L21 39Z"/><path d="M12 12L30 30M30 12L12 30"/></svg></div>
    <h3>Paving</h3>
    <p>Lorem ipsum dolor sit amet, consectetur adipiscing elit, sed do eiusmod tempor incididunt ut labore et dolore magna aliqua. Quis ipsum suspendisse ultrices gravida. Risus commodo viverra maecenas accumsan lacus vel facilisis.</p>
    <div class="card-btn">Read More</div>
  </div>

  <!-- projects -->
  <section class="projects"></section>
  <h2 class="projects-title">OUR PROJECTS</h2>
  <div class="filters">
    <div class="pill on">ALL</div>
    <div class="pill">Driveways</div>
    <div class="pill">Fencing</div>
    <div class="pill">Paving</div>
  </div>
  <div class="proj-arrows">
    <svg width="34" height="20" viewBox="0 0 34 20" fill="none" stroke="#fff" stroke-width="2"><path d="M32 10H3M11 2L3 10L11 18"/></svg>
    <svg width="34" height="20" viewBox="0 0 34 20" fill="none" stroke="#fff" stroke-width="2"><path d="M2 10H31M23 2L31 10L23 18"/></svg>
  </div>
  <div class="projects-rule"></div>
  <div class="tile" style="left:135px;top:1952px;background:linear-gradient(160deg,#8a7a66,#6e5c48 45%,#4d8a34 70%,#b9ad9c)" role="img" aria-label="Timber fence with raised sleeper beds, lawn and grey patio"></div>
  <div class="tile" style="left:452px;top:1952px;background:linear-gradient(180deg,#56603e 0%,#6c6f4a 48%,#3f7a2a 52%,#5ea23a 100%)" role="img" aria-label="Garden before and after new lawn"></div>
  <div class="tile" style="left:770px;top:1952px;background:linear-gradient(150deg,#4a7a2c 0%,#b7b7b5 25%,#d2d2d0 60%,#a9a8a4 100%)" role="img" aria-label="Grey porcelain paving path beside lawn"></div>
  <div class="tile" style="left:135px;top:2272px;background:linear-gradient(160deg,#8a4a38,#a9917a 40%,#4b8a30 65%,#d6d4d0)" role="img" aria-label="Timber pergola over new patio next to brick house"></div>
  <div class="tile" style="left:452px;top:2272px;background:linear-gradient(170deg,#7fa6d0 0%,#c9b190 35%,#9d8466 65%,#5a4c40)" role="img" aria-label="Wooden pergola with fence panels and outdoor seating"></div>
  <div class="tile" style="left:770px;top:2272px;background:linear-gradient(150deg,#7a5e5a,#8e6f6c 50%,#6b5a5c)" role="img" aria-label="Freshly laid block-paved driveway"></div>

  <!-- faq -->
  <h2 class="h2" style="left:214px;top:2727px">Frequently Asked Question</h2>
  <div class="acc" style="top:2795px">01. Kerspiciatis unde omnis iste natus erty?<span class="sign">+</span></div>
  <div class="acc open" style="top:2834px">02. Sed ut perspiciatis unde omnis iste natus error?<span class="sign">&minus;</span></div>
  <div class="acc-body">Sed ut perspiciatis unde omnis iste natus error sit voluptatem accusa nt ium dolorem que laudantium totam rem aperiamSed ut perspiciatis unde omnis iste natus error sit voluptatem accusa nt ium dolorem que laudantium totam rem aperiamue laudantium totam rem aperiamSed ut perspiciatis unde omnis istety.</div>
  <div class="acc" style="top:2990px">03. Unde omnis iste natused perspiciatis ?<span class="sign">+</span></div>
  <div class="acc" style="top:3029px">04. Sedperspiciatis unde omnis ister?<span class="sign">+</span></div>

  <h2 class="h2" style="left:610px;top:2727px">Request An Estimate</h2>
  <div class="field" style="left:610px;top:2794px;width:180px;height:31px">Name*</div>
  <div class="field" style="left:802px;top:2794px;width:184px;height:31px">E-mail*</div>
  <div class="field" style="left:610px;top:2842px;width:376px;height:31px;justify-content:space-between">Select Subject<svg width="8" height="5" viewBox="0 0 8 5"><path d="M0 0H8L4 5Z" fill="#666"/></svg></div>
  <div class="field" style="left:610px;top:2890px;width:376px;height:123px;align-items:flex-start;padding-top:12px">Message</div>
  <div class="submit">SUBMIT</div>

  <!-- testimonials -->
  <div class="t-eyebrow">What users say</div>
  <h2 class="t-title">More then 30k+ peoples<br>love our services</h2>
  <svg class="abs" style="left:290px;top:3383px" width="34" height="18" viewBox="0 0 34 18" fill="none" stroke="#999" stroke-width="1.5"><path d="M32 9H3M10 2L3 9L10 16"/></svg>
  <svg class="abs" style="left:878px;top:3383px" width="34" height="18" viewBox="0 0 34 18" fill="none" stroke="#999" stroke-width="1.5"><path d="M2 9H31M24 2L31 9L24 16"/></svg>
  <div class="t-card"></div>
  <div class="t-photo" role="img" aria-label="Smiling couple holding their small dog"></div>
  <svg class="t-quote" width="58" height="44" viewBox="0 0 58 44" fill="#6cbe45"><path d="M2 2H24V24C24 34 18 40 8 42L6 36C12 34 14 30 14 26H2Z"/><path d="M32 2H54V24C54 34 48 40 38 42L36 36C42 34 44 30 44 26H32Z"/></svg>
  <p class="t-text">Helps you keep your inspiration in the same place from pictures to links, texts and colors. Inspiration comes in many ways and you like to save.</p>
  <div class="t-stars">&#9733;&#9733;&#9733;&#9733;&#9733;</div>
  <div class="t-name">Daniel Marsh</div>

  <!-- footer -->
  <footer class="footer"></footer>
  <div class="f-brand"><span class="brand-dot"></span>Brackwell<br>Landscapes</div>
  <div class="f-contact">
    <div><svg width="11" height="11" viewBox="0 0 12 12" fill="none" stroke="#fff" stroke-width="1.2"><circle cx="6" cy="6" r="5.2"/><path d="M4 3.5l1 1.5-.6.8c.5.9 1 1.4 1.9 1.9l.8-.6 1.5 1-.6 1.1c-2.3-.3-4.3-2.3-4.6-4.6z" fill="#fff" stroke="none"/></svg>07700 900 418</div>
    <div><svg width="11" height="11" viewBox="0 0 12 12" fill="none" stroke="#fff" stroke-width="1.2"><circle cx="6" cy="6" r="5.2"/><rect x="3" y="4" width="6" height="4"/><path d="M3 4l3 2 3-2"/></svg>info@brackwell-landscapes.com</div>
    <div><svg width="11" height="11" viewBox="0 0 12 12" fill="none" stroke="#fff" stroke-width="1.2"><circle cx="6" cy="6" r="5.2"/><path d="M1 6h10M6 1c-2 2.5-2 7.5 0 10M6 1c2 2.5 2 7.5 0 10"/></svg>brackwell-landscapes.com</div>
  </div>
  <nav class="f-nav">
    <div>Home</div><div>Our Services</div><div>About Us</div><div>Our Projects</div><div>FAQ</div>
  </nav>
  <div class="f-notify">
    <h4>Be Notified</h4>
    <p>Enter you email address to be notified of the launch</p>
  </div>
  <div class="f-input">Your Mail</div>
  <div class="f-btn">Notify</div>
  <div class="f-copy">2020 Copyright Brackwell Landscapes - All Rights</div>

</div>
</body>
</html>
```